Etiketten auf Kühlschrank Wasserfilter Velmiro
Zielgruppe
Wasserfilter Velmiro
Aufgabenstellung
Ich brauche eine neue Etikette auf Kühlschrank Wasserfilter Velmiro. die Massse der Etikette muss gleiche wie die alte Etikett.

```html
<!DOCTYPE html>
<html lang="en">
<head>
<meta charset="utf-8">
<title>Velmiro Refrigerator Water Filter Label</title>
<link rel="stylesheet" href="https://fonts.googleapis.com/css2?family=Montserrat:wght@400;500;700;800&display=swap">
<style>
  :root {
    --page: #ffffff;
    --navy: #1c3a78;
    --ink: #1f3f75;
    --ribbon: #2d77b8;
    --sky-edge: #3a6cae;
    --sky-mid: #dceaf6;
    --deep: #123e86;
    --white: #ffffff;
    --badge-ring: #f2b632;
    --badge-green: #1f9a3e;
  }
  html, body {
    margin: 0;
    padding: 0;
    width: 1200px;
    height: 1137px;
    overflow: hidden;
    background: var(--page);
    font-family: "Montserrat", Arial, sans-serif;
  }
  .canvas {
    position: relative;
    width: 1200px;
    height: 1137px;
  }
  .label {
    position: absolute;
    left: 73px;
    top: 43px;
    width: 1003px;
    height: 1001px;
    transform: scale(1.05);
    transform-origin: top left;
    overflow: hidden;
    box-shadow: 0 10px 30px rgba(0,0,0,0.25);
    background: linear-gradient(90deg, var(--sky-edge) 0%, #9cbfe2 25%, var(--sky-mid) 55%, #a8c7e6 80%, var(--sky-edge) 100%);
  }
  .label__sky-fade {
    position: absolute;
    inset: 0;
    background: linear-gradient(180deg, rgba(40,90,160,0.55) 0%, rgba(255,255,255,0) 30%, rgba(255,255,255,0.35) 55%, rgba(255,255,255,0) 62%);
  }
  .label__water {
    position: absolute;
    left: 0;
    top: 600px;
    width: 1003px;
    height: 401px;
    background:
      radial-gradient(ellipse 70% 40% at 50% 10%, rgba(190,220,245,0.9), rgba(190,220,245,0) 70%),
      linear-gradient(180deg, #5b8fcb 0%, #2a63ac 35%, var(--deep) 70%, #0f3677 100%);
  }
  .ribbon {
    position: absolute;
    left: 82px;
    top: 0;
    width: 272px;
    height: 248px;
  }
  .ribbon__name {
    position: absolute;
    left: 0;
    top: 70px;
    width: 272px;
    text-align: center;
    color: var(--white);
    font-weight: 700;
    font-size: 40px;
    letter-spacing: 0.5px;
  }
  .title {
    position: absolute;
    left: 386px;
    top: 44px;
    margin: 0;
    color: var(--white);
    font-weight: 700;
    font-size: 40px;
    letter-spacing: 0.3px;
    white-space: nowrap;
  }
  .compat {
    position: absolute;
    left: 408px;
    top: 108px;
    width: 504px;
    height: 96px;
    background: var(--white);
    color: var(--ink);
    font-size: 29px;
    line-height: 37px;
    text-align: center;
    display: flex;
    flex-direction: column;
    justify-content: center;
  }
  .compat sup { font-size: 14px; }
  .specs {
    position: absolute;
    left: 43px;
    top: 285px;
    width: 915px;
    border-collapse: collapse;
    color: var(--navy);
    font-size: 28px;
  }
  .specs td {
    border: 3px solid var(--navy);
    height: 56px;
    padding: 0 10px 0 11px;
    white-space: nowrap;
    background: rgba(255,255,255,0.12);
  }
  .specs .specs__head td { height: 66px; font-weight: 700; padding-left: 14px; }
  .specs b { font-weight: 700; }
  .specs span { font-weight: 500; }
  .badges {
    position: absolute;
    left: 0;
    top: 640px;
    width: 1003px;
    height: 180px;
  }
  .badge { position: absolute; top: 0; }
  .badge__caption {
    position: absolute;
    left: 0;
    top: 150px;
    width: 160px;
    text-align: center;
    color: var(--white);
    font-weight: 700;
    font-size: 17px;
  }
  .disclaimer {
    position: absolute;
    left: 0;
    top: 828px;
    width: 1003px;
    margin: 0;
    text-align: center;
    color: var(--white);
    font-size: 16.5px;
    line-height: 21px;
    font-weight: 500;
  }
  .install {
    position: absolute;
    left: 221px;
    top: 897px;
    width: 562px;
    height: 60px;
    background: var(--white);
    border-radius: 30px;
    color: var(--ribbon);
  }
  .install__lock, .install__start {
    position: absolute;
    top: 0;
    line-height: 60px;
    font-size: 34px;
  }
  .install__lock { left: 40px; }
  .install__start { left: 439px; }
  .install__arrow { position: absolute; left: 160px; top: 2px; }
</style>
</head>
<body>
<main class="canvas">
  <section class="label">
    <div class="label__sky-fade"></div>
    <div class="label__water" role="img" aria-label="Photograph of clear blue water waves"></div>

    <div class="ribbon">
      <svg width="272" height="248" viewBox="0 0 272 248">
        <polygon points="0,0 272,0 272,248 136,178 0,248" fill="var(--ribbon)"/>
      </svg>
      <div class="ribbon__name">Velmiro</div>
    </div>

    <h1 class="title">Refrigerator Water Filter</h1>
    <div class="compat">
      <div>Replacement for</div>
      <div>Norvik<sup>®</sup> filter NV29-00020B</div>
    </div>

    <table class="specs">
      <tr class="specs__head"><td>Application Guidelines | Water Supply Parameters</td></tr>
      <tr><td><b>Flow rate:</b> <span>0.55 GPM | 2.1 LPM</span></td></tr>
      <tr><td><b>Operating Temperature:</b> <span>34°F - 100°F | 1°C - 38°C</span></td></tr>
      <tr><td><b>Operating Pressure:</b> <span>30 PSI - 120 PSI | 207 kPa - 827 kPa</span></td></tr>
      <tr><td><b>Capacity:</b> <span>300 Gallons or 1135 liters</span></td></tr>
    </table>

    <div class="badges">
      <div class="badge" style="left:97px">
        <svg width="160" height="160" viewBox="0 0 160 160" role="img" aria-label="Replacement interval badge">
          <circle cx="80" cy="80" r="74" fill="none" stroke="var(--white)" stroke-width="5"/>
        </svg>
      </div>
      <div class="badge" style="left:313px">
        <svg width="160" height="160" viewBox="0 0 160 160" role="img" aria-label="Recycling badge">
          <circle cx="80" cy="80" r="68" fill="var(--badge-green)"/>
        </svg>
      </div>
      <div class="badge" style="left:528px">
        <svg width="160" height="160" viewBox="0 0 160 160" role="img" aria-label="Food contact safety badge">
          <rect x="10" y="6" width="140" height="130" fill="none" stroke="var(--white)" stroke-width="6"/>
        </svg>
        <div class="badge__caption">EC 1935/2004</div>
      </div>
      <div class="badge" style="left:743px">
        <svg width="160" height="160" viewBox="0 0 160 160" role="img" aria-label="Quality management certification badge">
          <circle cx="80" cy="86" r="74" fill="var(--white)" stroke="var(--badge-ring)" stroke-width="6"/>
        </svg>
      </div>
    </div>

    <p class="disclaimer">* All trademarks remain the property of their respective holder(s) and are used for compatibility information only.<br>Claims of compatibility verified through manufacture testing.</p>

    <div class="install">
      <span class="install__lock">Lock</span>
      <svg class="install__arrow" width="240" height="56" viewBox="0 0 240 56">
        <rect x="0" y="16" width="210" height="24" fill="var(--ribbon)"/>
        <polygon points="208,0 240,28 208,56" fill="var(--ribbon)"/>
        <text x="105" y="35" text-anchor="middle" fill="var(--white)" font-family="Montserrat, Arial, sans-serif" font-size="19" font-weight="500">Install</text>
      </svg>
      <span class="install__start">Start</span>
    </div>
  </section>
</main>
</body>
</html>
```